Billboard design for dentist that sees only children

I own a 12' x 25' digital billboard and I need help with billboard design. My wife is a general dentist that only sees children and is very passionate about giving them a quality dental experience . She has a great reputation in town. Obviously with a billboard there can't be a lot of reading. Maybe something that shows safety, love, experience and children. I am completely open to your ideas. In addition I have other businesses that also need billboard design so this could lead to more work. If you go to Maplecovedental.com under the about section you will find more information about the practice and our phone number. Attached is our logo which could be changed and content specs for the digital billboard. Happy Designing!!

Target Market(s)

Parents with children

Colors

Designer to choose colors to be used in the design.

Requirements
Must have
• Must attract attention and be nice to look at.
Nice to have
• Probably should have children in the picture ..... Maybe
Should not have
• If I see something I don't like I will let you know

```html
<!DOCTYPE html>
<html lang="en">
<head>
<meta charset="utf-8">
<title>Maple Cove Dental – Billboard Designs</title>
<link rel="stylesheet" href="https://fonts.googleapis.com/css2?family=Lato:wght@400;700;900&display=swap">
<style>
  :root {
    --stage: #000000;
    --panel-top: #f0f5f4;
    --panel-bottom: #95c2bb;
    --headline: #1f4a86;
    --brand-teal: #3a7e72;
    --call-box: #3e7a68;
    --call-text: #ffffff;
    --address: #262626;
    --arc-navy: #141a55;
    --arc-blue: #2a8ee0;
  }
  * { margin: 0; padding: 0; box-sizing: border-box; }
  html, body {
    width: 1200px;
    height: 1200px;
    overflow: hidden;
    background: var(--stage);
    font-family: "Lato", sans-serif;
  }
  .stage { position: relative; width: 1200px; height: 1200px; }

  .billboard {
    position: absolute;
    left: 73px;
    width: 1046px;
    height: 502px;
    overflow: hidden;
    background: linear-gradient(180deg, var(--panel-top) 0%, var(--panel-bottom) 100%);
  }
  .billboard--first { top: 77px; }
  .billboard--second { top: 614px; }

  .billboard__art {
    position: absolute;
    inset: 0;
    width: 1046px;
    height: 502px;
  }

  .brand {
    position: absolute;
    left: 55px;
    top: 54px;
    display: flex;
    align-items: center;
    gap: 14px;
  }
  .brand__dot {
    width: 64px;
    height: 64px;
    border-radius: 50%;
    background: var(--brand-teal);
  }
  .brand__text { display: flex; flex-direction: column; align-items: flex-end; }
  .brand__name {
    font-weight: 400;
    font-size: 41px;
    line-height: 1;
    color: var(--brand-teal);
    letter-spacing: 0.5px;
  }
  .brand__tagline {
    font-weight: 400;
    font-size: 18px;
    line-height: 1.1;
    color: var(--brand-teal);
    letter-spacing: 0.5px;
  }

  .headline {
    position: absolute;
    left: 20px;
    width: 518px;
    top: 154px;
    text-align: center;
    font-weight: 900;
    font-size: 58px;
    line-height: 62px;
    color: var(--headline);
    letter-spacing: -0.5px;
    white-space: nowrap;
  }

  .call-box {
    position: absolute;
    left: 103px;
    top: 372px;
    width: 354px;
    height: 54px;
    background: var(--call-box);
    color: var(--call-text);
    font-weight: 900;
    font-size: 36px;
    line-height: 54px;
    text-align: center;
    white-space: nowrap;
  }

  .address {
    position: absolute;
    left: 30px;
    width: 500px;
    top: 449px;
    text-align: center;
    font-weight: 400;
    font-size: 19px;
    color: var(--address);
    white-space: nowrap;
  }
</style>
</head>
<body>
<main class="stage">

  <section class="billboard billboard--first">
    <svg class="billboard__art" viewBox="0 0 1046 502" xmlns="http://www.w3.org/2000/svg">
      <defs>
        <clipPath id="photo-area-a">
          <path d="M652,0 Q475,255 585,502 L1046,502 L1046,0 Z"/>
        </clipPath>
        <linearGradient id="photo-base-a" x1="0" y1="0" x2="1" y2="1">
          <stop offset="0" stop-color="#f4efea"/>
          <stop offset="1" stop-color="#e8dccf"/>
        </linearGradient>
        <radialGradient id="photo-hair-a" cx="0.5" cy="0.45" r="0.5">
          <stop offset="0" stop-color="#e2b48f"/>
          <stop offset="0.6" stop-color="#e6c79a"/>
          <stop offset="0.85" stop-color="#d8b37a"/>
          <stop offset="1" stop-color="#d8b37a" stop-opacity="0"/>
        </radialGradient>
        <radialGradient id="photo-skin-a" cx="0.5" cy="0.5" r="0.5">
          <stop offset="0" stop-color="#f2cdb6"/>
          <stop offset="0.7" stop-color="#ecc0a3"/>
          <stop offset="1" stop-color="#ecc0a3" stop-opacity="0"/>
        </radialGradient>
        <linearGradient id="arc-band-a" x1="0" y1="0" x2="0" y2="1">
          <stop offset="0" stop-color="var(--arc-navy)"/>
          <stop offset="0.55" stop-color="var(--arc-blue)"/>
          <stop offset="1" stop-color="var(--arc-navy)"/>
        </linearGradient>
      </defs>
      <g clip-path="url(#photo-area-a)" role="img" aria-label="Photo of a smiling blonde girl pointing to a gap in her teeth">
        <rect x="500" y="0" width="546" height="502" fill="url(#photo-base-a)"/>
        <ellipse cx="880" cy="270" rx="260" ry="330" fill="url(#photo-hair-a)"/>
        <ellipse cx="880" cy="300" rx="170" ry="210" fill="url(#photo-skin-a)"/>
        <rect x="600" y="470" width="446" height="32" fill="#c97b78" opacity="0.35"/>
      </g>
      <path d="M642,0 Q420,255 568,502 L585,502 Q475,255 652,0 Z" fill="url(#arc-band-a)"/>
    </svg>

    <div class="brand">
      <span class="brand__dot"></span>
      <div class="brand__text">
        <span class="brand__name">Maple Cove Dental</span>
        <span class="brand__tagline">general dentistry for children</span>
      </div>
    </div>
    <h1 class="headline">Comfortable<br>Dental Care for<br>your Child</h1>
    <div class="call-box">Call: 555.014.2876</div>
    <p class="address">428 North Linden Avenue, Fairhaven, NM 88120</p>
  </section>

  <section class="billboard billboard--second">
    <svg class="billboard__art" viewBox="0 0 1046 502" xmlns="http://www.w3.org/2000/svg">
      <defs>
        <clipPath id="photo-area-b">
          <path d="M652,0 Q475,255 585,502 L1046,502 L1046,0 Z"/>
        </clipPath>
        <radialGradient id="photo-hair-b" cx="0.5" cy="0.5" r="0.5">
          <stop offset="0" stop-color="#8a6450"/>
          <stop offset="0.75" stop-color="#6e4c3c"/>
          <stop offset="1" stop-color="#6e4c3c" stop-opacity="0"/>
        </radialGradient>
        <radialGradient id="photo-skin-b" cx="0.5" cy="0.5" r="0.5">
          <stop offset="0" stop-color="#f3cdb8"/>
          <stop offset="0.7" stop-color="#eab9a0"/>
          <stop offset="1" stop-color="#eab9a0" stop-opacity="0"/>
        </radialGradient>
        <radialGradient id="photo-dress-b" cx="0.5" cy="0.5" r="0.5">
          <stop offset="0" stop-color="#f6d3e2"/>
          <stop offset="0.75" stop-color="#f0c2d4"/>
          <stop offset="1" stop-color="#f0c2d4" stop-opacity="0"/>
        </radialGradient>
        <linearGradient id="arc-band-b" x1="0" y1="0" x2="0" y2="1">
          <stop offset="0" stop-color="var(--arc-navy)"/>
          <stop offset="0.55" stop-color="var(--arc-blue)"/>
          <stop offset="1" stop-color="var(--arc-navy)"/>
        </linearGradient>
      </defs>
      <g clip-path="url(#photo-area-b)" role="img" aria-label="Photo of a girl with braids in a floral dress showing her missing front teeth">
        <rect x="500" y="0" width="546" height="502" fill="#ffffff"/>
        <ellipse cx="880" cy="500" rx="250" ry="150" fill="url(#photo-dress-b)"/>
        <ellipse cx="880" cy="230" rx="190" ry="230" fill="url(#photo-hair-b)"/>
        <ellipse cx="880" cy="270" rx="130" ry="170" fill="url(#photo-skin-b)"/>
      </g>
      <path d="M642,0 Q420,255 568,502 L585,502 Q475,255 652,0 Z" fill="url(#arc-band-b)"/>
    </svg>

    <div class="brand">
      <span class="brand__dot"></span>
      <div class="brand__text">
        <span class="brand__name">Maple Cove Dental</span>
        <span class="brand__tagline">general dentistry for children</span>
      </div>
    </div>
    <h2 class="headline">Comfortable<br>Dental Care for<br>your Child</h2>
    <div class="call-box">Call: 555.014.2876</div>
    <p class="address">428 North Linden Avenue, Fairhaven, NM 88120</p>
  </section>

</main>
</body>
</html>
```